Flyer-Design für Lindauer Hotel
Zielgruppe
Lindauer Hotel
Aufgabenstellung
Texte: siehe alten Fyler,
drei Sterne dürfen nicht mehr in den Texten auftauchen.
www.lindauer-hotel-beispiel.de

```html
<!DOCTYPE html>
<html lang="de">
<head>
<meta charset="utf-8">
<title>Lindauer Hotel – Flyer</title>
<link href="https://fonts.googleapis.com/css2?family=Roboto:wght@400;500&family=Pinyon+Script&display=swap" rel="stylesheet">
<style>
  :root {
    --gold: #a97c3c;
    --gold-dark: #8e6630;
    --cream: #f6e6c8;
    --cream-light: #fbf1de;
    --ink: #3a2f22;
    --stage: #e4e4e4;
  }
  * { box-sizing: border-box; margin: 0; padding: 0; }
  html, body { width: 1200px; height: 847px; overflow: hidden; }
  body {
    background: var(--stage);
    font-family: "Roboto", Arial, sans-serif;
    color: var(--ink);
  }
  .flyer {
    position: absolute;
    left: 200px; top: 23px;
    width: 800px; height: 800px;
    display: flex;
    box-shadow: 0 6px 24px rgba(0,0,0,.18);
  }
  .panel {
    position: relative;
    width: 400px; height: 800px;
    overflow: hidden;
    background: var(--cream);
  }
  .panel__backdrop {
    position: absolute; inset: 0;
    background: linear-gradient(160deg, var(--cream-light) 0%, #f1dcb5 45%, #efe3c4 70%, #f3e6cb 100%);
  }
  .band {
    position: relative;
    background: var(--gold);
    color: #fff;
    display: flex; align-items: center; justify-content: center;
  }
  /* Left panel */
  .band--find { height: 82px; gap: 18px; }
  .band--find h2 { font-weight: 400; font-size: 17px; letter-spacing: .5px; }
  .contact { position: relative; padding: 26px 30px 0; text-align: center; }
  .contact h3 { color: var(--gold); font-weight: 500; font-size: 18px; margin-bottom: 8px; }
  .contact p { font-size: 11.5px; line-height: 1.6; }
  .contact .dot { color: var(--gold); }
  .map {
    position: relative;
    margin: 16px 30px 0;
    height: 170px;
    border: 1.5px solid var(--gold);
    border-radius: 12px;
    background: linear-gradient(135deg, #f3ead0, #eadfb9);
  }
  .map__note {
    position: absolute; right: 14px; top: 12px;
    font-size: 10px; color: var(--ink); text-align: left;
    background: rgba(251,241,222,.85); padding: 4px 6px; border-radius: 4px;
  }
  .prices {
    position: relative;
    margin: 22px 0 0;
    border-top: 1px solid var(--gold);
    padding: 16px 30px 0;
    height: 190px;
  }
  .prices h4, .services h4 { color: var(--gold); font-weight: 400; font-size: 15px; }
  .services { position: relative; padding: 0 30px; }
  .services__grid {
    margin-top: 10px;
    display: grid; grid-template-columns: repeat(7, 36px); gap: 10px 9px;
  }
  .icon {
    width: 36px; height: 36px;
    border: 1.5px solid var(--gold);
    border-radius: 6px;
    display: flex; align-items: center; justify-content: center;
  }
  .icon svg { width: 24px; height: 24px; stroke: var(--gold); fill: none; stroke-width: 2; }
  .band--foot { position: absolute; left: 0; right: 0; bottom: 0; height: 86px; gap: 10px; }
  .wordmark { font-size: 20px; font-weight: 400; color: #fff; }
  .wordmark-dot { width: 14px; height: 14px; border-radius: 50%; background: var(--ink); }
  /* Right panel */
  .band--head { height: 70px; gap: 10px; }
  .photo {
    position: relative; height: 330px;
    background: linear-gradient(180deg, #b9cfe0 0%, #c9b7a4 35%, #e9e5df 60%, #5a7f98 85%, #b95a4e 100%);
  }
  .welcome { position: relative; text-align: center; padding-top: 70px; }
  .welcome__kicker { font-size: 15px; letter-spacing: .5px; color: var(--gold-dark); }
  .welcome__name {
    font-family: "Pinyon Script", cursive;
    font-size: 46px; color: var(--gold-dark);
    margin: 14px 0 12px; font-weight: 400;
  }
  .welcome__place { font-size: 15px; letter-spacing: .5px; color: var(--gold-dark); }
  .band--url { position: absolute; left: 0; right: 0; bottom: 0; height: 70px; font-size: 16px; }
</style>
</head>
<body>
<div class="flyer">

  <section class="panel panel--back">
    <div class="panel__backdrop" role="img" aria-label="Blasses Foto eines Holzschilds mit der Aufschrift Welcome"></div>
    <header class="band band--find">
      <h2>SO FINDEN SIE UNS:</h2>
      <svg width="34" height="42" viewBox="0 0 34 42" aria-hidden="true">
        <path d="M17 2a14 14 0 0 1 14 14c0 10-14 22-14 22S3 26 3 16A14 14 0 0 1 17 2z" fill="#fff"/>
        <circle cx="17" cy="16" r="6" fill="#a97c3c"/>
      </svg>
    </header>

    <div class="contact">
      <h3>Lindauer Hotel in Vechta</h3>
      <p>Jonas Brandt <span class="dot">•</span> Lindenallee 27 <span class="dot">•</span> 49300 Vechta Deutschland<br>
      Telefon: +49 (0) 4400-123450 <span class="dot">•</span> Telefax: +49 (0) 4400-123459</p>
    </div>

    <div class="map" role="img" aria-label="Lageplan mit Straßen, Parkplatz und Hotelstandort">
      <p class="map__note">Parkplatz ist in der Gartenstraße 18<br>(am Ende einer Sackgasse)</p>
    </div>

    <div class="prices">
      <h4>Unsere Preise:</h4>
    </div>

    <div class="services">
      <h4>Hoteldienstleistungen</h4>
      <div class="services__grid">
        <div class="icon"><svg viewBox="0 0 24 24"><circle cx="8" cy="6" r="3"/><path d="M3 21v-7h10v7M15 10h6v11"/></svg></div>
        <div class="icon"><svg viewBox="0 0 24 24"><path d="M5 4h4l2 5-3 2a11 11 0 0 0 5 5l2-3 5 2v4a2 2 0 0 1-2 2A17 17 0 0 1 3 6a2 2 0 0 1 2-2z"/></svg></div>
        <div class="icon"><svg viewBox="0 0 24 24"><circle cx="12" cy="13" r="7"/><path d="M12 9v4l3 2M5 4l3 2M19 4l-3 2"/></svg></div>
        <div class="icon"><svg viewBox="0 0 24 24"><path d="M3 9a13 13 0 0 1 18 0M6 13a8 8 0 0 1 12 0M9 17a3 3 0 0 1 6 0"/></svg></div>
        <div class="icon"><svg viewBox="0 0 24 24"><path d="M8 20V4h6a4 4 0 0 1 0 8H8"/></svg></div>
        <div class="icon"><svg viewBox="0 0 24 24"><rect x="3" y="6" width="18" height="12" rx="1"/><path d="M3 7l9 6 9-6"/></svg></div>
        <div class="icon"><svg viewBox="0 0 24 24"><circle cx="12" cy="12" r="9"/><path d="M6 6l12 12"/></svg></div>
        <div class="icon"><svg viewBox="0 0 24 24"><path d="M4 10h12v6a4 4 0 0 1-4 4H8a4 4 0 0 1-4-4zM16 12h3v3h-3M8 4v3M12 4v3"/></svg></div>
        <div class="icon"><svg viewBox="0 0 24 24"><path d="M3 20V8M21 20V8M3 16h18M3 10h18M8 10v6M13 10v6"/></svg></div>
        <div class="icon"><svg viewBox="0 0 24 24"><path d="M4 6h12l3 3-3 3H9l-2 8H4z"/></svg></div>
        <div class="icon"><svg viewBox="0 0 24 24"><rect x="4" y="3" width="16" height="18"/><path d="M12 3v18M8 9l-1 2h2zM16 11l-1-2-1 2"/></svg></div>
        <div class="icon"><svg viewBox="0 0 24 24"><rect x="3" y="7" width="14" height="10" rx="1"/><path d="M3 11h14M19 9l2 8"/></svg></div>
        <div class="icon"><svg viewBox="0 0 24 24"><circle cx="8" cy="15" r="4"/><path d="M11 12l8-8M16 7l2 2"/></svg></div>
        <div class="icon"><svg viewBox="0 0 24 24"><circle cx="12" cy="12" r="9"/><path d="M6 13h11M6 6l12 12"/></svg></div>
      </div>
    </div>

    <footer class="band band--foot">
      <span class="wordmark">Lindauer Hotel</span><span class="wordmark-dot"></span>
    </footer>
  </section>

  <section class="panel panel--front">
    <div class="panel__backdrop" role="img" aria-label="Blasses Foto eines Holzschilds mit der Aufschrift Welcome"></div>
    <header class="band band--head">
      <span class="wordmark">Lindauer Hotel</span><span class="wordmark-dot"></span>
    </header>
    <div class="photo" role="img" aria-label="Foto der Hotelfassade in der Fußgängerzone mit Bogenfenstern und Ladenschildern"></div>
    <div class="welcome">
      <p class="welcome__kicker">HERZLICH WILLKOMMEN IM</p>
      <h1 class="welcome__name">Lindauer Hotel Garni</h1>
      <p class="welcome__place">IN VECHTA</p>
    </div>
    <footer class="band band--url">www.lindauer-hotel-beispiel.de</footer>
  </section>

</div>
</body>
</html>
```